Need simple and modern looking business card with all my information on one side and logo on the other side
Info :
Company name - VELMAR CONSTRUCTION LLC
Company addres- 418 harbor 87th. Dunmoor park ny 10352
Email- velmarllc@tridomail.Com
Company phone number 555-318-6094
Cell number- 555-742-0583
Web site - velmarllc.Com
My name Gerald tomasino

Target Market(s)

Construction , home improvement, remodeling

Industry/Entity Type

Construction

Contact Information for Business Card

It has to be moder but at the same time simple

Font styles to use
Sans Serif

Colors
0255a3
ffffff
000000
f78f20
b1b1b1
9d9d9d
1b1b1b
33a6d7
ec1f27

Requirements
Must have
• My logo on one side maybe with a some kind of background on the other side all my information
Nice to have
• Some kind of background pictures provided by you .PLEASE HAVE ACCOUNT WITH PIXELVAULT WILL NOT PAY ANY EXTRA FEES .
Should not have
• Any kind of hamer, nails,screws, helmets itp. Please do not copy the other designs come up with something new.

```html
<!DOCTYPE html>
<html lang="en">
<head>
<meta charset="utf-8">
<title>Velmar Construction LLC – Business Card</title>
<link rel="stylesheet" href="https://fonts.googleapis.com/css2?family=Arimo:wght@400;700&display=swap">
<style>
  :root {
    --orange: #f78f20;
    --orange-deep: #e27a0e;
    --white: #ffffff;
    --black: #000000;
    --ink: #1b1b1b;
    --grey-light: #b1b1b1;
    --grey: #9d9d9d;
    --backdrop: #3a3a3c;
    --card-w: 720px;
    --card-h: 411px;
  }
  * { box-sizing: border-box; margin: 0; padding: 0; }
  html, body {
    width: 1200px;
    height: 950px;
    overflow: hidden;
  }
  body {
    background: var(--backdrop);
    font-family: "Arimo", Arial, sans-serif;
    display: flex;
    flex-direction: column;
    align-items: center;
    justify-content: center;
    gap: 44px;
  }
  .card {
    position: relative;
    width: var(--card-w);
    height: var(--card-h);
    overflow: hidden;
    box-shadow: 0 10px 30px rgba(0,0,0,.35);
  }

  /* Back side */
  .card--back {
    background: linear-gradient(160deg, var(--orange) 0%, var(--orange-deep) 100%);
    display: flex;
    flex-direction: column;
    align-items: center;
    justify-content: center;
    color: rgba(255,255,255,.88);
    text-align: center;
  }
  .back-brand__name {
    font-weight: 700;
    font-size: 78px;
    letter-spacing: 4px;
    line-height: 1;
  }
  .back-brand__sub {
    font-weight: 700;
    font-size: 28px;
    letter-spacing: 3px;
    margin-top: 6px;
  }
  .back-site {
    margin-top: 26px;
    font-size: 20px;
    letter-spacing: 2px;
  }

  /* Front side */
  .card--front { background: var(--black); }
  .front-top {
    position: absolute;
    inset: 0 0 auto 0;
    height: 228px;
    background: var(--white);
  }
  .front-divider {
    position: absolute;
    left: 0; top: 216px;
    width: 100%; height: 20px;
  }
  .brand {
    position: absolute;
    top: 70px;
    left: 200px;
    width: 460px;
    color: var(--ink);
    text-align: center;
  }
  .brand__name {
    font-weight: 700;
    font-size: 74px;
    letter-spacing: 5px;
    line-height: 1;
  }
  .brand__sub {
    font-weight: 700;
    font-size: 25px;
    letter-spacing: 2px;
    margin-top: 4px;
  }
  .holder {
    position: absolute;
    left: 44px;
    top: 254px;
    color: var(--white);
    font-size: 19px;
    line-height: 1.3;
  }
  .holder__name {
    color: var(--orange);
    font-weight: 700;
    font-size: 25px;
    margin-bottom: 2px;
  }
  .contacts {
    position: absolute;
    right: 32px;
    bottom: 30px;
    list-style: none;
    color: var(--grey-light);
    font-size: 19px;
  }
  .contacts li {
    display: flex;
    align-items: center;
    justify-content: flex-end;
    gap: 14px;
    height: 28px;
  }
  .contacts svg { width: 18px; height: 18px; flex: none; }
</style>
</head>
<body>

  <section class="card card--back" aria-label="Business card, logo side">
    <div class="back-brand">
      <div class="back-brand__name">VELMAR</div>
      <div class="back-brand__sub">CONSTRUCTION LLC</div>
    </div>
    <div class="back-site">velmarllc.Com</div>
  </section>

  <section class="card card--front" aria-label="Business card, information side">
    <div class="front-top"></div>
    <svg class="front-divider" viewBox="0 0 720 20" preserveAspectRatio="none" aria-hidden="true">
      <path d="M0 12 H50 L60 2 L70 12 H720" fill="none" stroke="var(--orange)" stroke-width="2.5"/>
    </svg>

    <div class="brand">
      <div class="brand__name">VELMAR</div>
      <div class="brand__sub">CONSTRUCTION LLC</div>
    </div>

    <div class="holder">
      <div class="holder__name">Gerald tomasino</div>
      <div class="holder__title">CEO/Founder</div>
      <div class="holder__address">418 harbor 87th.<br>Dunmoor park ny 10352</div>
    </div>

    <ul class="contacts">
      <li>555-318-6094
        <svg viewBox="0 0 20 20" aria-hidden="true"><path d="M5 3 L8 3 L9 7 L7 8.5 C8 11 9 12 11.5 13 L13 11 L17 12 V15 C17 16 16 17 15 17 C9 16.5 3.5 11 3 5 C3 4 4 3 5 3 Z" fill="var(--orange)"/></svg>
      </li>
      <li>555-742-0583
        <svg viewBox="0 0 20 20" aria-hidden="true"><rect x="6" y="2" width="8" height="16" rx="1.5" fill="var(--orange)"/><rect x="7.3" y="4" width="5.4" height="10" fill="var(--black)"/></svg>
      </li>
      <li>velmarllc@tridomail.Com
        <svg viewBox="0 0 20 20" aria-hidden="true"><rect x="2" y="5" width="16" height="11" fill="var(--orange)"/><path d="M2 5 L10 11 L18 5" fill="none" stroke="var(--black)" stroke-width="1.3"/></svg>
      </li>
      <li>velmarllc.Com
        <svg viewBox="0 0 20 20" aria-hidden="true"><circle cx="10" cy="10" r="8" fill="var(--orange)"/><ellipse cx="10" cy="10" rx="3.2" ry="8" fill="none" stroke="var(--black)" stroke-width="1.2"/><path d="M2 10 H18" stroke="var(--black)" stroke-width="1.2"/></svg>
      </li>
    </ul>
  </section>

</body>
</html>
```